Business Card and Letterhead for new HR Consultancy

A business card and letterhead design that includes the logo (attached in jpg) and the business tag line which is "Investing in Your Greatest Asset"
We are based in regional New South Wales, Australia and provide HR services to small and medium business owners to support them grow their businesses by focusing on their people. The services provided cover the full range of HR management from simple advice through to comprehensive programs that support people management. My clients typically will not have a HR manager, either because they don't need to employ one or can't afford to hire one. So they will be looking for me to provide good services, add value to their business for a competitive price.
I am a middle aged woman with over 15 years expertise in all facets of HR Management. My clients need to know they can trust me, that I am credible and competent and open in my relationship with them and that I can make a positive difference for them.
I would like to see designs that are modern and communicate value for money.
A note to advise that the email address is
xxxxxxx@wattlecrestteam.com.au
website will be
www.wattlecrestteam.com.au
thanks
L.
Will also need to include the business number (indicates it is a registered business).
ABN: 38 217 405 963
Target Market(s)
small to medium sized business owners 30 years and over, professional and tradespeople
Industry/Entity Type
Business
Look and feel

```html
<!DOCTYPE html>
<html lang="en">
<head>
<meta charset="utf-8">
<title>Wattlecrest Team — Business Card</title>
<link rel="stylesheet" href="https://fonts.googleapis.com/css2?family=Arimo:ital,wght@0,400;0,700;1,400&display=swap">
<style>
  :root {
    --brand-green: #22c00c;
    --text-dark: #33373a;
    --bg-center: #ffffff;
    --bg-edge: #c4c4c4;
    --icon-light: #e9e9e9;
    --icon-dark: #8d8d8d;
  }
  html, body {
    margin: 0;
    padding: 0;
    width: 1200px;
    height: 695px;
    overflow: hidden;
  }
  .card {
    position: relative;
    width: 1200px;
    height: 695px;
    background: radial-gradient(ellipse 75% 70% at 50% 48%, var(--bg-center) 55%, var(--bg-edge) 100%);
    font-family: "Arimo", Arial, sans-serif;
    overflow: hidden;
  }
  .brand-mark {
    position: absolute;
    left: 60px;
    top: 248px;
    width: 84px;
    height: 84px;
    border-radius: 50%;
    background: var(--brand-green);
  }
  .brand-name {
    position: absolute;
    left: 166px;
    top: 246px;
    margin: 0;
    font-size: 66px;
    font-weight: 700;
    line-height: 1;
    letter-spacing: -1px;
    color: var(--brand-green);
    white-space: nowrap;
  }
  .tagline {
    position: absolute;
    left: 221px;
    top: 376px;
    margin: 0;
    font-size: 35px;
    font-style: italic;
    line-height: 1;
    color: var(--brand-green);
    white-space: nowrap;
  }
  .divider {
    position: absolute;
    left: 771px;
    top: 112px;
    width: 7px;
    height: 476px;
    background: var(--brand-green);
  }
  .person-name {
    position: absolute;
    left: 801px;
    top: 166px;
    margin: 0;
    font-size: 55px;
    font-weight: 400;
    line-height: 1;
    color: var(--brand-green);
  }
  .person-role {
    position: absolute;
    left: 802px;
    top: 225px;
    margin: 0;
    font-size: 31px;
    line-height: 1;
    color: var(--brand-green);
  }
  .contact-list {
    position: absolute;
    left: 802px;
    top: 302px;
    margin: 0;
    padding: 0;
    list-style: none;
  }
  .contact-item {
    position: absolute;
    left: 0;
    display: flex;
    align-items: flex-start;
    white-space: nowrap;
  }
  .contact-item.phone { top: 0; }
  .contact-item.email { top: 70px; }
  .contact-item.address { top: 143px; }
  .contact-icon {
    width: 41px;
    height: 41px;
    flex: none;
    margin-right: 12px;
  }
  .contact-text {
    font-size: 34px;
    line-height: 39px;
    color: var(--text-dark);
  }
</style>
</head>
<body>
<main class="card">
  <section class="brand">
    <span class="brand-mark" aria-hidden="true"></span>
    <h1 class="brand-name">Wattlecrest Team</h1>
    <p class="tagline">Investing in Your Greatest Asset</p>
  </section>

  <div class="divider" aria-hidden="true"></div>

  <section class="contact">
    <h2 class="person-name">Your Name</h2>
    <p class="person-role">HR Manager</p>

    <svg width="0" height="0" style="position:absolute" aria-hidden="true">
      <defs>
        <linearGradient id="icon-fill" x1="0" y1="0" x2="0" y2="1">
          <stop offset="0" stop-color="#e6e6e6"/>
          <stop offset="1" stop-color="#7f7f7f"/>
        </linearGradient>
        <linearGradient id="paper-fill" x1="0" y1="0" x2="0" y2="1">
          <stop offset="0" stop-color="#ffffff"/>
          <stop offset="1" stop-color="#dcdcdc"/>
        </linearGradient>
      </defs>
    </svg>

    <ul class="contact-list">
      <li class="contact-item phone">
        <svg class="contact-icon" viewBox="0 0 40 40" aria-hidden="true">
          <rect x="1" y="1" width="38" height="38" rx="7" fill="url(#icon-fill)" stroke="#6f6f6f"/>
          <path d="M12 8c-2 1-3 3-2.5 6 1.5 7 7.5 14 14.5 17 3 1 5 0 6.5-2l-4-5c-1 1-2.5 1.5-3.5 1-3-1.5-6-5-7-8-.3-1.2.5-2.5 1.5-3L14.5 8z" fill="#ffffff"/>
        </svg>
        <span class="contact-text">1234-1234</span>
      </li>
      <li class="contact-item email">
        <svg class="contact-icon" viewBox="0 0 40 40" aria-hidden="true">
          <path d="M3 16 L20 5 L37 16 V36 H3 Z" fill="url(#paper-fill)" stroke="#9a9a9a"/>
          <path d="M3 16 L20 27 L37 16" fill="none" stroke="#a8a8a8"/>
          <circle cx="20" cy="18" r="5" fill="none" stroke="#333" stroke-width="1.8"/>
          <circle cx="20" cy="18" r="2" fill="none" stroke="#333" stroke-width="1.5"/>
        </svg>
        <span class="contact-text">email@email.com</span>
      </li>
      <li class="contact-item address">
        <svg class="contact-icon" viewBox="0 0 40 40" aria-hidden="true">
          <rect x="1" y="1" width="38" height="38" rx="7" fill="url(#icon-fill)" stroke="#6f6f6f"/>
          <rect x="7" y="11" width="26" height="18" fill="#ffffff"/>
          <path d="M7 11 L20 22 L33 11 M7 29 L16 19 M33 29 L24 19" fill="none" stroke="#9a9a9a" stroke-width="1.4"/>
        </svg>
        <span class="contact-text">12 Street Road<br>Town&nbsp;&nbsp;NSW 4001</span>
      </li>
    </ul>
  </section>
</main>
</body>
</html>
```